Brightmoor Security Solutions window graphic

Looking for a graphic for my security company , Business for the back window of my truck. Make it look cool, please.

Call now for service (206) 555-0147
Brightmoorsecuritywa.example

“ Protection you can count on”

Target Market(s)

Auto security

Industry/Entity Type

Security

```html
<!DOCTYPE html>
<html lang="en">
<head>
<meta charset="utf-8">
<title>Brightmoor Security Solutions – Rear Window Graphic</title>
<link rel="stylesheet" href="https://fonts.googleapis.com/css2?family=Michroma&family=Kaushan+Script&family=Fredoka:wght@500&display=swap">
<style>
  :root {
    --page-bg: #d9dbde;
    --panel-black: #050505;
    --band-grey: #262626;
    --brand-orange: #e8421b;
    --ink-white: #ffffff;
    --emblem-shade: #3a3a3a;
  }
  * { margin: 0; padding: 0; box-sizing: border-box; }
  html, body {
    width: 1200px;
    height: 635px;
    overflow: hidden;
    background: var(--page-bg);
  }
  .window-graphic {
    position: absolute;
    left: 20px;
    top: 168px;
    width: 1160px;
    height: 290px;
  }
  .window-shape {
    position: absolute;
    inset: 0;
    width: 100%;
    height: 100%;
  }
  .side-emblem {
    position: absolute;
    top: 12px;
    width: 170px;
    height: 200px;
    border-radius: 40% 40% 20% 20%;
    background: radial-gradient(ellipse at center, var(--emblem-shade) 0%, rgba(40,40,40,0.15) 65%, transparent 100%);
    opacity: 0.6;
  }
  .side-emblem--left { left: 10px; }
  .side-emblem--right { right: 10px; }
  .brand-dot {
    position: absolute;
    left: 278px;
    top: 40px;
    width: 130px;
    height: 130px;
    border-radius: 50%;
    background: var(--brand-orange);
  }
  .brand-name {
    position: absolute;
    left: 500px;
    top: 42px;
    width: 420px;
    color: var(--brand-orange);
    font-family: "Michroma", sans-serif;
    font-weight: 400;
    text-transform: uppercase;
    text-align: center;
  }
  .brand-name__main {
    display: block;
    font-size: 38px;
    line-height: 50px;
    letter-spacing: 1px;
  }
  .brand-name__sub {
    display: block;
    margin-top: 6px;
    font-size: 17px;
    line-height: 22px;
    letter-spacing: 4px;
  }
  .tagline {
    position: absolute;
    left: 484px;
    top: 138px;
    width: 470px;
    color: var(--ink-white);
    font-family: "Kaushan Script", cursive;
    font-size: 40px;
    line-height: 56px;
    text-align: center;
    white-space: nowrap;
  }
  .tagline-swoosh {
    position: absolute;
    left: 890px;
    top: 162px;
    width: 130px;
    height: 50px;
  }
  .contact-line {
    position: absolute;
    left: 0;
    top: 232px;
    width: 100%;
    display: flex;
    justify-content: center;
    align-items: center;
    gap: 12px;
    font-family: "Fredoka", sans-serif;
    font-weight: 500;
    font-size: 29px;
    line-height: 36px;
    color: var(--brand-orange);
    white-space: nowrap;
  }
  .contact-line__icon { width: 30px; height: 30px; flex: none; }
  .contact-line__divider { color: var(--brand-orange); margin: 0 4px; }
  .contact-line__web { text-transform: uppercase; }
</style>
</head>
<body>
  <section class="window-graphic" aria-label="Brightmoor Security Solutions rear window graphic">
    <svg class="window-shape" viewBox="0 0 1160 290" aria-hidden="true">
      <path d="M0 290 L0 60 Q0 8 60 8 L1100 8 Q1160 8 1160 60 L1160 290 Z" fill="var(--panel-black)"/>
      <path d="M0 281 L156 217 L1013 217 L1160 281 L1160 290 L0 290 Z" fill="var(--band-grey)"/>
      <path d="M0 281 L156 217 L1013 217 L1160 281" fill="none" stroke="var(--brand-orange)" stroke-width="3.5"/>
    </svg>

    <div class="side-emblem side-emblem--left" role="img" aria-label="Faint decorative brand emblem on the left"></div>
    <div class="side-emblem side-emblem--right" role="img" aria-label="Faint decorative brand emblem on the right"></div>

    <div class="brand-dot" aria-hidden="true"></div>
    <h1 class="brand-name">
      <span class="brand-name__main">Brightmoor</span>
      <span class="brand-name__sub">Security Solutions</span>
    </h1>

    <p class="tagline">Protection you can count on</p>
    <svg class="tagline-swoosh" viewBox="0 0 130 50" aria-hidden="true">
      <path d="M10 42 Q70 46 124 14 Q110 30 40 40 Q22 42 10 42 Z" fill="var(--ink-white)"/>
    </svg>

    <p class="contact-line">
      <svg class="contact-line__icon" viewBox="0 0 30 30" aria-hidden="true">
        <path d="M7 4 L11 4 L13 10 L10 12 Q12 18 18 20 L20 17 L26 19 L26 23 Q26 26 22 26 Q6 24 4 8 Q4 4 7 4 Z" fill="var(--ink-white)"/>
        <path d="M17 8 Q22 9 22 14 M17 3 Q27 4 27 14" fill="none" stroke="var(--ink-white)" stroke-width="1.8" stroke-linecap="round"/>
      </svg>
      <span class="contact-line__phone">(206) 555-0147</span>
      <span class="contact-line__divider">|</span>
      <svg class="contact-line__icon" viewBox="0 0 30 30" aria-hidden="true">
        <g fill="none" stroke="var(--ink-white)" stroke-width="1.6">
          <circle cx="15" cy="15" r="12"/>
          <ellipse cx="15" cy="15" rx="5.5" ry="12"/>
          <path d="M3 15 H27 M5 9 H25 M5 21 H25 M15 3 V27"/>
        </g>
      </svg>
      <span class="contact-line__web">Brightmoorsecuritywa.example</span>
    </p>
  </section>
</body>
</html>
```